We’re a real estate firm that has landed a big builder in a neighboring state. Our branding needs...

We are a real estate firm who represents various builders along with doing resale here in Oregon. Our firm is growing to represent a big builder in Washington State and we’ll have another 40 brokers on our team. We need rebranding. As in, a new logo ( the house logo we have now looks cartoonish, hate it). We need new cards, something to really stand out. I’ve been thinking of using those NFC cards from ZIB or the ones with the seam color. I likely want two or three designs, a darker (as in a background color of black or grey) , a light one ( again I mean background color) and a credit card style (either plastic w an embossed name/number on front, or metal ). I’m thinking dark background for cc, or silver if it’s metal. That’s my thoughts, but you are the artists, so maybe you have an idea I haven’t considered. Our colors were black and red, but we don’t have to stick to that. Just nothing too busy. Oh, and we are typically representing the local, higher quality builders in our area (just below custom), but not national. Subdivisions are near the Kel Varsby, Tobrin, and Ashfield Coastal sites. We are super excited, but without a lot of time to change the “look” of our brokerage. So I’ll be deciding and moving forward within 24 hours tops. Our name is Real Estate Summitline Partners ( we cant change the name because of timeline and business license) Thank you!

Industry/Entity Type

Real Estate

Contact Information for Business Card

The usual. Name of firm. Name of cardholder. Contact info.

Font styles to use
Serif
Sans Serif

Colors

Designer to choose colors to be used in the design.

Requirements
Must have
• A sleek or simple look. I included photos of cards with stylistic attributes we like. Thank you
Nice to have
• We really like the black backgrounds. With foil or embossed detail. We also like the black on black. Matte black card with raised shiny black detail. But still eye catching.
Should not have
• No ornate or busy looking style. We don’t want anything cluttered.

```html
<!DOCTYPE html>
<html lang="en">
<head>
<meta charset="utf-8">
<title>Real Estate Summitline Partners — Business Cards</title>
<link href="https://fonts.googleapis.com/css2?family=Montserrat:wght@400;600;700&display=swap" rel="stylesheet">
<style>
  :root {
    --backdrop: #2f2f31;
    --card: #1b1b1d;
    --card-edge: #262628;
    --red: #e5232b;
    --white: #f2f2f2;
    --silver: #9a9a9c;
    --muted: #d9d9d9;
  }
  * { box-sizing: border-box; margin: 0; padding: 0; }
  html, body {
    width: 1200px; height: 895px; overflow: hidden;
    background: var(--backdrop);
    font-family: "Montserrat", sans-serif;
  }
  .sheet {
    width: 1200px; height: 895px;
    display: flex; flex-direction: column;
    align-items: center; justify-content: center; gap: 56px;
  }
  .card {
    width: 620px; height: 354px;
    background: var(--card);
    border: 1px solid var(--card-edge);
    border-radius: 20px;
    box-shadow: 0 14px 30px rgba(0,0,0,.45);
    position: relative;
  }
  /* front */
  .card--front { display: flex; align-items: center; justify-content: center; }
  .brand {
    display: flex; align-items: center; gap: 14px;
    font-weight: 700; text-transform: uppercase;
  }
  .brand__mark { width: 16px; height: 16px; flex: none; }
  .brand__name { line-height: 1.15; letter-spacing: 1px; }
  .card--front .brand__mark { background: var(--silver); }
  .card--front .brand__name { color: var(--silver); font-size: 30px; width: 330px; }
  /* back */
  .card--back { display: flex; align-items: center; }
  .card--back .brand { width: 300px; justify-content: center; padding-left: 26px; }
  .card--back .brand__mark { background: var(--red); width: 12px; height: 12px; }
  .card--back .brand__name { color: var(--red); font-size: 21px; width: 230px; }
  .divider { width: 1px; height: 200px; background: var(--white); margin: 0 34px 0 18px; }
  .details { color: var(--muted); font-size: 13.5px; line-height: 1.35; }
  .holder__name { color: var(--red); font-weight: 700; font-size: 20px; text-transform: uppercase; letter-spacing: .5px; }
  .holder__title { color: var(--white); font-size: 14px; margin-bottom: 22px; }
  .address { margin-bottom: 20px; }
  .contact { list-style: none; }
  .contact li { display: flex; align-items: center; gap: 10px; margin-bottom: 3px; }
  .contact svg { width: 12px; height: 12px; fill: var(--red); flex: none; }
</style>
</head>
<body>
<main class="sheet">
  <section class="card card--front">
    <div class="brand">
      <span class="brand__mark"></span>
      <span class="brand__name">Real Estate Summitline Partners</span>
    </div>
  </section>

  <section class="card card--back">
    <div class="brand">
      <span class="brand__mark"></span>
      <span class="brand__name">Real Estate Summitline Partners</span>
    </div>
    <div class="divider"></div>
    <div class="details">
      <p class="holder__name">Marlo Trevick</p>
      <p class="holder__title">Founder &amp; CEO</p>
      <p class="address">4870 Alder Crest Way, Suite 118<br>Salem, OR 97301</p>
      <ul class="contact">
        <li><svg viewBox="0 0 24 24"><path d="M6.6 10.8a15.1 15.1 0 0 0 6.6 6.6l2.2-2.2c.3-.3.7-.4 1-.2 1.1.4 2.3.6 3.6.6.6 0 1 .4 1 1V20c0 .6-.4 1-1 1A17 17 0 0 1 3 4c0-.6.4-1 1-1h3.5c.6 0 1 .4 1 1 0 1.3.2 2.5.6 3.6.1.3 0 .7-.2 1z"/></svg>000 000 0000</li>
        <li><svg viewBox="0 0 24 24"><path d="M2 5h20v14H2zm2 2v.5l8 5 8-5V7l-8 5z"/></svg>info@summitlinere.com</li>
        <li><svg viewBox="0 0 24 24"><path d="M12 2a10 10 0 1 0 0 20 10 10 0 0 0 0-20zm0 2c.9 1.2 1.6 2.9 1.9 5h-3.8c.3-2.1 1-3.8 1.9-5zM4.3 13h3.8a18 18 0 0 0 0-2H4.3a8 8 0 0 0 0 2zm1-4h3c.2-1.7.7-3.2 1.3-4.3A8 8 0 0 0 5.3 9zm4.8 2a16 16 0 0 0 0 2h3.8a16 16 0 0 0 0-2zm5.8 0a18 18 0 0 1 0 2h3.8a8 8 0 0 0 0-2zm-.2-2h3a8 8 0 0 0-4.3-4.3c.6 1.1 1.1 2.6 1.3 4.3zM5.3 15a8 8 0 0 0 4.3 4.3c-.6-1.1-1.1-2.6-1.3-4.3zm4.8 0c.3 2.1 1 3.8 1.9 5 .9-1.2 1.6-2.9 1.9-5zm5.6 0c-.2 1.7-.7 3.2-1.3 4.3a8 8 0 0 0 4.3-4.3z"/></svg>www.summitlinere.com</li>
      </ul>
    </div>
  </section>
</main>
</body>
</html>
```